Marcus Tellow album cover "Borrowed Lanterns, Quiet Harbors"

3000x3000 album cover using attached image and provided text needed for cover of upcoming album for Seattle musician. Only front cover needed at this time.

Font styles to use
Serif
Sans Serif

Colors

Designer to choose colors to be used in the design.

```html
<!DOCTYPE html>
<html lang="en">
<head>
<meta charset="utf-8">
<title>Marcus Tellow – Borrowed Lanterns, Quiet Harbors</title>
<link rel="stylesheet" href="https://fonts.googleapis.com/css2?family=Roboto:wght@400;500&display=swap">
<style>
  :root {
    --sky-deep: #0f2236;
    --sky-blue: #1d3c5c;
    --tree-dark: #1f2a1c;
    --lamp-amber: #c98a3a;
    --trailer-glow: #e9dcc4;
    --grass-olive: #6e6a2c;
    --grass-dark: #3a3a1a;
    --frame-line: rgba(255, 255, 255, 0.9);
    --veil: rgba(255, 255, 255, 0.42);
    --ink: #141414;
  }
  * { margin: 0; padding: 0; box-sizing: border-box; }
  html, body { width: 1200px; height: 1200px; overflow: hidden; background: #000; }
  .cover {
    position: relative;
    width: 1200px;
    height: 1200px;
    overflow: hidden;
    font-family: "Roboto", Arial, sans-serif;
  }
  .cover-photo {
    position: absolute;
    inset: 0;
    background:
      radial-gradient(ellipse 38% 26% at 52% 60%, rgba(240, 228, 205, 0.85), rgba(240, 228, 205, 0) 70%),
      radial-gradient(ellipse 20% 30% at 94% 58%, rgba(214, 150, 70, 0.75), rgba(214, 150, 70, 0) 70%),
      radial-gradient(ellipse 30% 10% at 18% 49%, rgba(205, 130, 70, 0.6), rgba(205, 130, 70, 0) 70%),
      linear-gradient(180deg,
        var(--sky-deep) 0%,
        var(--sky-blue) 14%,
        var(--tree-dark) 30%,
        #4a3a22 40%,
        #6b4a2e 50%,
        var(--lamp-amber) 62%,
        var(--grass-olive) 78%,
        var(--grass-dark) 100%);
  }
  .outer-frame {
    position: absolute;
    left: 24px; top: 24px;
    width: 1152px; height: 1152px;
    border: 1.5px solid var(--frame-line);
  }
  .title-veil {
    position: absolute;
    left: 288px; top: 288px;
    width: 624px; height: 624px;
    background: var(--veil);
  }
  .title-frame {
    position: absolute;
    left: 274px; top: 274px;
    width: 652px; height: 652px;
    border: 1.5px solid var(--frame-line);
  }
  .artist-name {
    position: absolute;
    left: 0; right: 0;
    top: 372px;
    text-align: center;
    font-size: 25px;
    font-weight: 400;
    letter-spacing: 0.5px;
    color: var(--ink);
    text-transform: uppercase;
  }
  .name-rule {
    position: absolute;
    left: 565px; top: 412px;
    width: 70px; height: 2px;
    background: var(--ink);
  }
  .album-title {
    position: absolute;
    left: 0; right: 0;
    top: 556px;
    text-align: center;
    font-size: 43px;
    font-weight: 500;
    line-height: 61px;
    color: var(--ink);
  }
</style>
</head>
<body>
  <main class="cover">
    <div class="cover-photo" role="img" aria-label="Night photograph of a vintage camper trailer glowing under floodlight in a grassy campground, with a warm-lit cabin on the left, a silver trailer on the right and tall trees against a deep blue sky"></div>
    <div class="outer-frame"></div>
    <div class="title-veil"></div>
    <div class="title-frame"></div>
    <p class="artist-name">Marcus Tellow</p>
    <div class="name-rule"></div>
    <h1 class="album-title">Borrowed Lanterns,<br>Quiet Harbors</h1>
  </main>
</body>
</html>
```